BRUNDOVIX Label and bottle design

We have already provided attached an idea concept of a label and bottle shape example, we now require designers to take this basic concept and advance it to the final label design using your own design creativity.
Please see attached the full product brief

```html
<!DOCTYPE html>
<html lang="en">
<head>
<meta charset="utf-8">
<title>BRUNDOVIX Ink Verra Label</title>
<link rel="stylesheet" href="https://fonts.googleapis.com/css2?family=Montserrat:ital,wght@0,500;0,600;0,800;1,600&family=Oswald:wght@500;600&display=swap">
<style>
  :root {
    --bg: #2b2b2b;
    --label: #0d0d0d;
    --label-soft: #161616;
    --yellow: #f7ec1a;
    --yellow-deep: #d9cb10;
    --silver: #b9b9b9;
    --white: #ffffff;
    --ink-dark: #111111;
    --uv-blue: #1f5fa8;
    --solvent-green: #2f8a49;
    --water-blue: #1d64b0;
  }
  * { box-sizing: border-box; margin: 0; padding: 0; }
  html, body { width: 964px; height: 1200px; overflow: hidden; background: var(--bg); }
  .canvas { position: relative; width: 964px; height: 1200px; }
  .label {
    position: absolute; left: 182px; top: 41px; width: 600px; height: 1118px;
    background: radial-gradient(ellipse at 50% 40%, var(--label-soft), var(--label) 75%);
    overflow: hidden; font-family: "Montserrat", sans-serif; color: var(--white);
  }
  .brand {
    position: absolute; top: 120px; left: 0; width: 100%; text-align: center;
    font-family: "Montserrat", sans-serif; font-weight: 800; font-size: 78px;
    letter-spacing: 1px; color: var(--yellow);
  }
  .tagline {
    position: absolute; top: 298px; left: 0; width: 100%; text-align: center;
    font-style: italic; font-weight: 600; font-size: 31px; line-height: 47px; letter-spacing: 0.5px;
  }
  .swoosh { position: absolute; left: 0; width: 600px; }
  .swoosh-top { top: 378px; height: 74px; }
  .swoosh-bottom { top: 594px; height: 74px; }
  .product-name {
    position: absolute; top: 470px; left: 0; width: 100%; text-align: center;
    font-family: "Oswald", sans-serif; font-weight: 600; font-size: 96px; letter-spacing: 3px; line-height: 110px;
  }
  .product-name .accent { color: var(--yellow); }
  .descriptor {
    position: absolute; top: 642px; left: 0; width: 100%; text-align: center;
    font-weight: 500; font-size: 32px; line-height: 40px; letter-spacing: 0.5px;
  }
  .suitable {
    position: absolute; top: 748px; left: 85px; width: 430px;
    display: flex; align-items: center; gap: 14px;
    color: var(--yellow); font-size: 20px; font-weight: 500; letter-spacing: 0.5px;
  }
  .suitable .rule { flex: 1; height: 1px; background: var(--yellow-deep); }
  .ink-types { position: absolute; top: 800px; left: 57px; display: flex; gap: 34px; }
  .ink-badge {
    width: 133px; height: 143px; border-radius: 14px; border: 3px solid #ffffff33;
    display: flex; flex-direction: column; align-items: center; justify-content: flex-end;
    padding-bottom: 14px; font-family: "Oswald", sans-serif; font-weight: 500;
    font-size: 17px; line-height: 22px; text-align: center; position: relative; overflow: hidden;
  }
  .ink-badge svg { position: absolute; top: 10px; left: 41px; }
  .ink-badge.uv { background: linear-gradient(170deg, #eaf2fb 0 38%, var(--uv-blue) 40%); color: var(--white); }
  .ink-badge.solvent { background: linear-gradient(170deg, #e4f1e7 0 38%, var(--solvent-green) 40%); color: var(--white); }
  .ink-badge.water { background: var(--white); border-color: var(--water-blue); color: var(--water-blue); }
  .pro-use {
    position: absolute; top: 980px; left: 70px; width: 460px;
    display: flex; align-items: center; gap: 16px;
    font-weight: 600; font-size: 25px; letter-spacing: 0.5px;
  }
  .pro-use .rule { width: 46px; height: 2px; background: var(--white); }
  .pro-use .text { flex: 1; text-align: center; }
  .base-line { position: absolute; top: 1037px; left: 0; width: 100%; height: 5px;
    background: linear-gradient(90deg, #6e6608, var(--yellow-deep) 50%, #6e6608); }
  .net-weight {
    position: absolute; top: 1053px; left: 0; width: 100%; height: 65px; background: var(--yellow);
    color: var(--ink-dark); text-align: center; font-family: "Oswald", sans-serif;
    font-weight: 600; font-size: 50px; line-height: 65px; letter-spacing: 0.5px;
  }
</style>
</head>
<body>
<main class="canvas">
  <section class="label">
    <div class="brand">BRUNDOVIX</div>
    <p class="tagline">PROFESSIONAL CLEANING<br>MAXIMUM PERFORMANCE</p>

    <svg class="swoosh swoosh-top" viewBox="0 0 600 74" aria-hidden="true">
      <rect x="0" y="0" width="600" height="74" fill="#f7ec1a"/>
      <path d="M0 0 H600 V18 Q300 90 0 18 Z" fill="#bbbbbb"/>
      <path d="M0 0 H600 V6 Q300 82 0 6 Z" fill="#0d0d0d"/>
      <path d="M0 74 V52 Q300 80 600 52 V74 Z" fill="#0d0d0d"/>
    </svg>

    <h1 class="product-name"><span class="accent">INK</span> VERRA</h1>

    <svg class="swoosh swoosh-bottom" viewBox="0 0 600 74" aria-hidden="true">
      <rect x="0" y="0" width="600" height="74" fill="#f7ec1a"/>
      <path d="M0 0 V18 Q300 -6 600 18 V0 Z" fill="#0d0d0d"/>
      <path d="M0 74 V56 Q300 -16 600 56 V74 Z" fill="#bbbbbb"/>
      <path d="M0 74 V68 Q300 -4 600 68 V74 Z" fill="#0d0d0d"/>
    </svg>

    <p class="descriptor">ADVANCED<br>ANILOX CLEANING GEL</p>

    <div class="suitable"><span class="rule"></span><span>SUITABLE FOR :</span><span class="rule"></span></div>

    <div class="ink-types">
      <div class="ink-badge uv">
        <svg width="46" height="62" viewBox="0 0 46 62" aria-hidden="true"><path d="M23 2 C14 20 4 30 4 41 a19 19 0 0 0 38 0 C42 30 32 20 23 2 Z" fill="#ffffff" stroke="#9fb6cf" stroke-width="2"/></svg>
        <span>UV-BASED<br>INKS</span>
      </div>
      <div class="ink-badge solvent">
        <svg width="46" height="62" viewBox="0 0 46 62" aria-hidden="true"><path d="M23 2 C14 20 4 30 4 41 a19 19 0 0 0 38 0 C42 30 32 20 23 2 Z" fill="#ffffff" stroke="#9fc9aa" stroke-width="2"/></svg>
        <span>SOLVENT-BASED<br>INKS</span>
      </div>
      <div class="ink-badge water">
        <svg width="46" height="62" viewBox="0 0 46 62" aria-hidden="true"><path d="M23 2 C14 20 4 30 4 41 a19 19 0 0 0 38 0 C42 30 32 20 23 2 Z" fill="#dfeaf7" stroke="#1d64b0" stroke-width="2"/></svg>
        <span>WATER-BASED<br>INKS</span>
      </div>
    </div>

    <div class="pro-use"><span class="rule"></span><span class="text">FOR PROFESSIONAL USE</span><span class="rule"></span></div>

    <div class="base-line"></div>
    <div class="net-weight">NET WT - 1KG</div>
  </section>
</main>
</body>
</html>
```